Simple proffessional BC

I have a logo which I will attach below.
I would like the logo on the front of the card with these details in point form below:
Pre and Post Natal Yoga: Pregnancy Workshops: Hypnobirthing Courses
On the back of the card my details:
Merrin Galvey
Facebook page- calmbellieswillowharbour
Mobile- 0438 512 740

I like the idea of the card being simple, possibly just the above on a plain coloured (eggshell?) card, a card that is textured.
I am open to suggestion if it appeals!
Thank you and good luck!

Target Market(s)

Pregnant women, 20's-40's

Requirements
Must have
• Simple, compliment logo.
Make logo the feature.
Should not have

• .

```html
<!DOCTYPE html>
<html lang="en">
<head>
<meta charset="utf-8">
<title>Calm Bellies – Business Card</title>
<link href="https://fonts.googleapis.com/css2?family=Quicksand:wght@300;400;500;600;700&display=swap" rel="stylesheet">
<style>
  :root {
    --page: #ffffff;
    --card: #fef5dc;
    --ink: #7a1c1c;
    --accent: #eea43a;
    --watermark: #fbe9c8;
  }
  * { margin: 0; padding: 0; box-sizing: border-box; }
  html, body {
    width: 1200px;
    height: 1000px;
    overflow: hidden;
    background: var(--page);
    font-family: "Quicksand", sans-serif;
    color: var(--ink);
  }
  .canvas { position: relative; width: 1200px; height: 1000px; }
  .card {
    position: absolute;
    width: 792px;
    height: 439px;
    background: var(--card);
    overflow: hidden;
  }
  .card--front { left: 203px; top: 27px; }
  .card--back { left: 205px; top: 518px; }

  .brand { position: absolute; left: 73px; top: 37px; display: flex; align-items: center; }
  .brand__dot {
    width: 120px; height: 120px; border-radius: 50%;
    background: var(--accent);
  }
  .brand__name {
    margin-left: 22px;
    font-size: 52px;
    font-weight: 500;
    line-height: 1;
    letter-spacing: 1px;
  }

  .services {
    position: absolute; left: 0; right: 0; top: 196px;
    list-style: none; text-align: center;
    font-size: 31px; font-weight: 600; line-height: 56px;
  }

  .backdrop-circle {
    position: absolute; left: 373px; top: 18px;
    width: 394px; height: 394px; border-radius: 50%;
    background: var(--watermark);
  }
  .contact { position: absolute; left: 38px; top: 118px; }
  .contact__name { font-size: 34px; font-weight: 700; line-height: 1; }
  .contact__label { font-size: 24px; font-weight: 700; line-height: 1; }
  .contact__value { font-size: 24px; font-weight: 300; line-height: 1; }
  .contact__facebook { margin-top: 46px; }
  .contact__facebook .contact__value { display: block; margin-top: 2px; font-size: 23px; }
  .contact__mobile { margin-top: 34px; font-size: 26px; }
  .contact__mobile .contact__label { font-size: 26px; }
  .contact__mobile .contact__value { font-size: 26px; }
</style>
</head>
<body>
<main class="canvas">
  <section class="card card--front">
    <div class="brand">
      <div class="brand__dot"></div>
      <div class="brand__name">Calm Bellies</div>
    </div>
    <ul class="services">
      <li>Pre and Post Natal Yoga:</li>
      <li>Pregnancy Workshops:</li>
      <li>Hypnobirthing Courses</li>
    </ul>
  </section>

  <section class="card card--back">
    <div class="backdrop-circle"></div>
    <div class="contact">
      <p class="contact__name">Merrin Galvey</p>
      <p class="contact__facebook">
        <span class="contact__label">Facebook page</span><span class="contact__value">:</span>
        <span class="contact__value">calmbellieswillowharbour</span>
      </p>
      <p class="contact__mobile">
        <span class="contact__label">Mobile</span>
        <span class="contact__value"> - 0438 512 740</span>
      </p>
    </div>
  </section>
</main>
</body>
</html>
```